pharmacy/travel clinic business card design

We need a business card for our new business called Merrow Travel Clinic and Pharmacy. Our primary focus is doing consultations for people before travelling internationally and providing vaccinations and prescriptions for them. While the business is considered a pharmacy, it has more the look and feel of a doctor's office. The design should communicate a professional and trustworthy feel. I have attached a copy of the logo we are going to be using.
Updates
Thanks for the submissions.  If you haven`t been eliminated you are one of the finalists.  Decision will likely be made tomorrow.

Target Market(s)
Customers, other health care professionals, travel agents
Industry/Entity Type
Clinic
Look and feel
Each slider illustrates characteristics of the customer's brand and the style your logo design should communicate.

```html
<!DOCTYPE html>
<html lang="en">
<head>
<meta charset="utf-8">
<title>Merrow Travel Clinic and Pharmacy – Business Card</title>
<link href="https://fonts.googleapis.com/css2?family=Lato:wght@400;700&display=swap" rel="stylesheet">
<style>
  :root {
    --page-bg: #e6e9ec;
    --card-white: #ffffff;
    --ink: #2b2b2b;
    --ink-soft: #444444;
    --brand-blue: #2a78c8;
    --rule-blue: #5aa9e0;
    --back-top: #2fa3e0;
    --back-bottom: #2c3fa8;
    --on-blue: #ffffff;
    --brand-green: #8cc63f;
  }
  * { margin: 0; padding: 0; box-sizing: border-box; }
  html, body {
    width: 1200px; height: 960px; overflow: hidden;
    background: var(--page-bg);
    font-family: "Lato", "Helvetica Neue", Arial, sans-serif;
  }
  .canvas {
    position: relative; width: 1200px; height: 960px;
    display: flex; flex-direction: column; align-items: center; justify-content: center; gap: 50px;
  }
  .card {
    position: relative; width: 700px; height: 400px;
    box-shadow: 0 6px 22px rgba(0,0,0,0.18);
    overflow: hidden;
  }
  /* Front */
  .card-front { background: var(--card-white); }
  .brand {
    position: absolute; display: flex; align-items: center; gap: 14px;
  }
  .brand-dot { width: 26px; height: 26px; border-radius: 50%; flex: none; }
  .brand-name { font-weight: 700; line-height: 1.08; }
  .card-front .brand { left: 44px; top: 48px; }
  .card-front .brand-dot { background: var(--brand-green); }
  .card-front .brand-name { color: var(--brand-blue); font-size: 34px; }
  .person { position: absolute; left: 44px; top: 232px; }
  .person-name { font-size: 32px; font-weight: 400; color: var(--ink); letter-spacing: 0.5px; }
  .person-role { font-size: 21px; color: var(--ink-soft); text-align: right; margin-top: 4px; }
  .contact {
    position: absolute; left: 405px; top: 206px; bottom: 40px;
    border-left: 2px solid var(--rule-blue);
    padding-left: 16px;
    font-size: 17px; color: var(--ink); line-height: 27px;
  }
  .contact-line { display: flex; align-items: center; gap: 10px; white-space: nowrap; }
  .contact-icon { width: 16px; height: 16px; flex: none; }
  .contact-web { font-weight: 700; }
  /* Back */
  .card-back {
    background: linear-gradient(170deg, var(--back-top) 0%, var(--back-bottom) 100%);
  }
  .card-back .brand { left: 110px; top: 150px; }
  .card-back .brand-dot { background: var(--on-blue); }
  .card-back .brand-name { color: var(--on-blue); font-size: 40px; }
</style>
</head>
<body>
<main class="canvas">
  <section class="card card-front" aria-label="Business card front">
    <div class="brand">
      <span class="brand-dot"></span>
      <p class="brand-name">Merrow Travel Clinic<br>and Pharmacy</p>
    </div>
    <div class="person">
      <p class="person-name">DANA WHITFIELD</p>
      <p class="person-role">Operation Manager</p>
    </div>
    <div class="contact">
      <p class="contact-line">
        <svg class="contact-icon" viewBox="0 0 16 16" aria-hidden="true"><rect x="2" y="1" width="12" height="14" rx="1.5" fill="none" stroke="#2a78c8" stroke-width="1.5"/><rect x="4.5" y="3.5" width="7" height="3" fill="#2a78c8"/><circle cx="5.5" cy="10" r="1" fill="#2a78c8"/><circle cx="8" cy="10" r="1" fill="#2a78c8"/><circle cx="10.5" cy="10" r="1" fill="#2a78c8"/></svg>
        (221) 33 412 76 18
      </p>
      <p class="contact-line">
        <svg class="contact-icon" viewBox="0 0 16 16" aria-hidden="true"><rect x="4" y="1" width="8" height="14" rx="1.5" fill="none" stroke="#2a78c8" stroke-width="1.5"/><rect x="5.5" y="3" width="5" height="6" fill="#2a78c8"/><circle cx="8" cy="12.3" r="1" fill="#2a78c8"/></svg>
        (221) 77 584 13 62
      </p>
      <p class="contact-line">
        <svg class="contact-icon" viewBox="0 0 16 16" aria-hidden="true"><rect x="1" y="3.5" width="14" height="9" fill="none" stroke="#2a78c8" stroke-width="1.5"/><path d="M1 3.5 L8 9 L15 3.5" fill="none" stroke="#2a78c8" stroke-width="1.5"/></svg>
        name@merrow-travel.com
      </p>
      <p class="contact-line">Avenue des Jardins - Port Vert</p>
      <p class="contact-line">BP 218 - City, Country</p>
      <p class="contact-line contact-web">www.merrow-travel.com</p>
    </div>
  </section>

  <section class="card card-back" aria-label="Business card back">
    <div class="brand">
      <span class="brand-dot"></span>
      <p class="brand-name">Merrow Travel Clinic<br>and Pharmacy</p>
    </div>
  </section>
</main>
</body>
</html>
```